Harborvale Ventures brochure for Investment partnership, young harold pembly

We need a brochure design to attract new investors for our investing partnership Called Harborvale Ventures. We are based in New Orleans, La. We primarily invest in stocks, bonds, and crypto but venture out into other categories as well. We would like to see designs with the black and gold like our logo. The final design should say new, fresh, sleek, tech, and honorable. BROUCHURE WILL BE 4 pages.or one folded sheet a paparer if that makes sense.
Updates

A chart showing Harborvale Ventures gains since 2019 28.6 percent and the TR 400 gAINS 7.1 PERCENT

Target Market(s)

Probable Investors

Industry/Entity Type

Financial Planning

Colors

Designer to choose only greyscale colors for use in the design.

Requirements
Must have
• Black and Gold accent. Stock market feel. Sleek, High tech, innovative, Intellgent design.
Nice to have
• Page colors possibly black.
Should not have
• Boring, Old school,

```html
<!DOCTYPE html>
<html lang="en">
<head>
<meta charset="utf-8">
<title>Harborvale Ventures — Partnership Brochure</title>
<link rel="stylesheet" href="https://fonts.googleapis.com/css2?family=Tinos:wght@400;700&display=swap">
<style>
  :root{
    --backdrop:#b8b7b9;
    --ink:#0a0a0a;
    --paper:#ffffff;
    --gold-light:#f3e27a;
    --gold:#d8b84a;
    --gold-deep:#a9842a;
    --text-dark:#1a1a1a;
    --text-light:#f4f4f4;
    --line:#3a3a3a;
  }
  *{margin:0;padding:0;box-sizing:border-box}
  html,body{width:858px;height:1200px;overflow:hidden}
  body{background:var(--backdrop);position:relative;font-family:"Tinos","Times New Roman",serif;color:var(--text-dark)}
  .page{position:absolute;width:373px;height:480px;overflow:hidden;background:var(--paper)}
  .page svg.art{position:absolute;inset:0;width:373px;height:480px}
  .page--about{left:57px;top:89px}
  .page--cover{left:450px;top:89px}
  .page--invite{left:57px;top:647px}
  .page--steps{left:449px;top:647px}
  .txt{position:absolute}
  .heading-gold{color:var(--gold);font-weight:700;font-size:13px;border-bottom:1.5px solid var(--gold);padding-bottom:1px;display:inline-block}
  .body-light{color:var(--text-light);font-size:9.3px;line-height:10.7px}
  .heading-dark{font-weight:700;font-size:13px;color:var(--text-dark);border-bottom:1.5px solid var(--gold);padding-bottom:1px;display:inline-block}
  .contact-list{list-style:none;font-size:13.5px;line-height:19px}
  .contact-list li{display:flex;align-items:center;gap:5px}
  .contact-list svg{width:14px;height:14px}
  .brand-name{position:absolute;text-align:center;color:var(--ink);font-weight:400;letter-spacing:.5px;line-height:1.1;transform:translate(-50%,-50%);white-space:nowrap}
  .brand-sub{display:block;letter-spacing:2px}
  .cover-tag{left:0;width:373px;text-align:center;font-size:11.2px;line-height:12.9px;text-transform:uppercase}
  .cover-rule{position:absolute;left:168px;top:410px;width:36px;height:2px;background:var(--gold)}
  .cover-title{left:0;width:373px;text-align:center;font-weight:700;font-size:18.8px;line-height:19px;text-transform:uppercase}
  .steps{list-style:none;font-size:10px;line-height:12px}
  .steps li{display:flex;margin-bottom:8px}
  .step-label{flex:0 0 50px;font-size:11.5px;display:flex;align-items:flex-start;gap:2px}
  .step-num{display:inline-block;width:13px;height:13px;background:linear-gradient(var(--gold-light),var(--gold-deep));text-align:center;line-height:13px;font-size:10.5px}
</style>
</head>
<body>

<svg width="0" height="0" style="position:absolute">
  <defs>
    <linearGradient id="goldFill" x1="0" y1="0" x2="0" y2="1">
      <stop offset="0" stop-color="#d9b84a"/>
      <stop offset=".45" stop-color="#f3e57c"/>
      <stop offset="1" stop-color="#a9842a"/>
    </linearGradient>
    <linearGradient id="photoStreet" x1="0" y1="0" x2="0" y2="1">
      <stop offset="0" stop-color="#9a9a9a"/><stop offset=".5" stop-color="#5a5a5a"/><stop offset="1" stop-color="#2a2a2a"/>
    </linearGradient>
    <linearGradient id="photoTram" x1="0" y1="0" x2="1" y2="1">
      <stop offset="0" stop-color="#5e5e5e"/><stop offset=".5" stop-color="#a8a8a8"/><stop offset="1" stop-color="#e2e2e2"/>
    </linearGradient>
    <linearGradient id="photoBridge" x1="0" y1="0" x2="0" y2="1">
      <stop offset="0" stop-color="#b0b0b0"/><stop offset=".55" stop-color="#6a6a6a"/><stop offset="1" stop-color="#2c2c2c"/>
    </linearGradient>
    <radialGradient id="photoTablet" cx=".5" cy=".5" r=".6">
      <stop offset="0" stop-color="#8a8a8a"/><stop offset="1" stop-color="#2a2a2a"/>
    </radialGradient>
    <linearGradient id="paperFade" x1="0" y1="0" x2="1" y2="0">
      <stop offset="0" stop-color="#ffffff"/><stop offset="1" stop-color="#e9e9e9"/>
    </linearGradient>
  </defs>
</svg>

<!-- Page 1: About -->
<section class="page page--about">
  <svg class="art" viewBox="0 0 373 480">
    <rect width="373" height="480" fill="var(--ink)"/>
    <path d="M0 190 Q150 120 373 250 L373 480 L0 480Z" fill="url(#paperFade)"/>
    <path d="M262 480 C290 450 308 410 306 370" fill="none" stroke="var(--line)" stroke-width="1"/>
    <circle cx="227" cy="252" r="130" fill="url(#photoStreet)" role="img" aria-label="Black and white photo of a historic French Quarter street with a cathedral"/>
    <circle cx="87" cy="311" r="59" fill="url(#goldFill)"/>
  </svg>
  <div class="txt" style="left:26px;top:32px"><span class="heading-gold">About us</span></div>
  <p class="txt body-light" style="left:26px;top:60px;width:288px">Harborvale Ventures was founded in 2019 by General Partner Darnell Whitaker Jr with a group economic empowerment mission. Darnell Whitaker has invested in stocks since a teenager, received his BA in economics from Bayou State University and is currently attending Gulf Coast University.</p>
  <div class="brand-name" style="left:87px;top:313px;font-size:14px">HARBORVALE<span class="brand-sub" style="font-size:7px">VENTURES</span></div>
  <div class="txt" style="left:26px;top:396px"><span class="heading-dark">Contact us</span></div>
  <ul class="txt contact-list" style="left:26px;top:420px">
    <li><svg viewBox="0 0 16 16"><circle cx="8" cy="8" r="7" fill="none" stroke="#222"/><path d="M5 4.5l1.6-.4 1 2-1 .8a5 5 0 002.5 2.5l.8-1 2 1-.4 1.6C8 11 5 8 5 4.5z" fill="#222"/></svg>0504-318-226</li>
    <li><svg viewBox="0 0 16 16"><circle cx="8" cy="8" r="7" fill="none" stroke="#222"/><rect x="4" y="5.2" width="8" height="5.6" fill="none" stroke="#222"/><path d="M4 5.2l4 3 4-3" fill="none" stroke="#222"/></svg>hello@harborvale-mail.com</li>
  </ul>
</section>

<!-- Page 2: Cover -->
<section class="page page--cover">
  <svg class="art" viewBox="0 0 373 480">
    <rect width="373" height="480" fill="url(#paperFade)"/>
    <circle cx="60" cy="90" r="185" fill="var(--ink)"/>
    <circle cx="227" cy="-12" r="206" fill="url(#photoTram)" role="img" aria-label="Black and white photo of a New Orleans streetcar on a palm-lined avenue"/>
    <circle cx="250" cy="490" r="245" fill="none" stroke="var(--line)" stroke-width="1"/>
    <circle cx="263" cy="261" r="83" fill="url(#goldFill)"/>
  </svg>
  <div class="brand-name" style="left:263px;top:263px;font-size:22px">HARBORVALE<span class="brand-sub" style="font-size:10px;letter-spacing:3px">VENTURES</span></div>
  <p class="txt cover-tag" style="top:365px">Become a partner<br>and build generational wealth by investing<br>in the stock market</p>
  <div class="cover-rule"></div>
  <h1 class="txt cover-title" style="top:419px">A first of its<br>kind investment club</h1>
</section>

<!-- Page 3: Invitation -->
<section class="page page--invite">
  <svg class="art" viewBox="0 0 373 480">
    <rect width="373" height="480" fill="url(#paperFade)"/>
    <circle cx="150" cy="60" r="300" fill="var(--ink)"/>
    <circle cx="120" cy="60" r="200" fill="none" stroke="#9a9a9a" stroke-width="1"/>
    <ellipse cx="160" cy="380" rx="190" ry="230" fill="url(#photoBridge)" role="img" aria-label="Black and white photo of a cable-stayed bridge and city skyline"/>
    <circle cx="259" cy="202" r="66" fill="url(#goldFill)"/>
  </svg>
  <p class="txt body-light" style="left:22px;top:43px;width:290px;font-size:9.8px;line-height:12px">If you are receiving this brochure it's because someone sees you as a person that doesn't want to just work and pay bills. Your someone who wants to build real generational wealth. Not through schemes but by using the greatest wealth builder available. The stock market.</p>
  <div class="brand-name" style="left:259px;top:205px;font-size:17px">HARBORVALE<span class="brand-sub" style="font-size:8.5px;letter-spacing:2.5px">VENTURES</span></div>
</section>

<!-- Page 4: How it works -->
<section class="page page--steps">
  <svg class="art" viewBox="0 0 373 480">
    <rect width="373" height="480" fill="url(#paperFade)"/>
    <path d="M0 0H80C40 80 30 200 0 267Z" fill="var(--ink)"/>
    <circle cx="186" cy="142" r="132" fill="url(#photoTablet)" role="img" aria-label="Black and white photo of hands holding a tablet showing a rising bar chart"/>
    <path d="M135 245 Q250 275 373 265" fill="none" stroke="var(--line)" stroke-width="1"/>
    <circle cx="265" cy="252" r="39" fill="var(--gold)" opacity=".6"/>
  </svg>
  <div class="txt" style="left:29px;top:273px"><span class="heading-dark">How it works</span></div>
  <ol class="txt steps" style="left:28px;top:301px;width:318px">
    <li><span class="step-label">STEP <span class="step-num">1</span></span><span>Make initial deposit. The general partner will invest in stocks, bonds and other investment vehicles on your behalf.</span></li>
    <li><span class="step-label">STEP <span class="step-num">2</span></span><span>There is no upfront fees. The general partner will guarantee a 5 percent return and will work for free on your behalf until that is achieved. After the 5 percent return on the dollars invested the limited partner will receive 80 percent and the general partner will receive 20 percent of every dollar gained.</span></li>
    <li><span class="step-label">STEP <span class="step-num">3</span></span><span>As the return and investments multiply the interests begins to compound annually. The legal partner legally owns shares of stock within the club and may redeem once a year or let money continue to earn interest.</span></li>
  </ol>
</section>

</body>
</html>
```